The Lantern Den Business Cards

We are a Craft Beer/Upscale dining Bar/Restaurant. We'll have 24 taps of craft beers and several types of bottled beers. In addition, we'll be serving a variety of top shelf bourbons, spirits and wines with a small unique menu. I'd like the design to be sophisticated, elegant and modern while staying away from "cartoonish" pictures.
Updates
Hello, I've added some example logos for inspiration. I'd like to use a lot of black/white with maybe a little color for a "pop". Thank you!
Industry/Entity Type
Business
Contact Information for Business Card
THE LANTERN DEN
Tomas Orlikova
582 Wexmoor Street
Norfolk, Virginia 23847
Office: (757) 555-0143
Mobile: (757) 555-0178
Look and feel
Each slider illustrates characteristics of the customer's brand and the style your logo design should communicate.

```html
<!DOCTYPE html>
<html lang="en">
<head>
<meta charset="utf-8">
<title>The Lantern Den – Business Card</title>
<link href="https://fonts.googleapis.com/css2?family=Arimo:wght@400;700&display=swap" rel="stylesheet">
<style>
  :root {
    --page-bg: #e4e2e0;
    --card-white: #ffffff;
    --card-black: #1a0f0e;
    --ink: #111111;
    --text-light: #f2f2f2;
    --text-soft: #d6d6d6;
  }
  * { margin: 0; padding: 0; box-sizing: border-box; }
  html, body {
    width: 1200px;
    height: 960px;
    overflow: hidden;
    background: var(--page-bg);
    font-family: "Arimo", Arial, sans-serif;
  }
  .stage {
    width: 1200px;
    height: 960px;
    display: flex;
    align-items: center;
    justify-content: center;
  }
  .business-card {
    width: 480px;
    height: 800px;
    border-radius: 28px;
    overflow: hidden;
    display: flex;
    flex-direction: column;
    box-shadow: 0 18px 40px rgba(0,0,0,0.25);
  }
  .card-top {
    height: 330px;
    background: var(--card-white);
    display: flex;
    align-items: center;
    justify-content: center;
    position: relative;
  }
  .brand-name {
    font-weight: 700;
    font-size: 34px;
    letter-spacing: 3px;
    color: var(--ink);
    text-align: center;
    line-height: 1.15;
  }
  .divider {
    position: absolute;
    left: 0; right: 0; bottom: 0;
    height: 18px;
    border-top: 2px solid var(--ink);
    border-bottom: 2px solid var(--ink);
    background: var(--card-white);
  }
  .card-bottom {
    flex: 1;
    background: var(--card-black);
    padding: 70px 56px 0 70px;
    color: var(--text-light);
  }
  .person-name {
    font-size: 38px;
    font-weight: 400;
    margin-bottom: 34px;
  }
  .contact-line {
    display: flex;
    align-items: center;
    gap: 16px;
    font-size: 26px;
    margin-bottom: 12px;
  }
  .contact-line svg { width: 26px; height: 26px; fill: var(--text-soft); flex: none; }
  .address {
    font-size: 22px;
    color: var(--text-soft);
    margin-top: 24px;
  }
</style>
</head>
<body>
<main class="stage">
  <article class="business-card">
    <section class="card-top">
      <h1 class="brand-name">THE<br>LANTERN DEN</h1>
      <div class="divider"></div>
    </section>
    <section class="card-bottom">
      <p class="person-name">Tomas Orlikova</p>
      <p class="contact-line">
        <svg viewBox="0 0 24 24" aria-hidden="true"><path d="M3 8c0-2 4-4 9-4s9 2 9 4v2h-5V8H8v2H3zM6 12h12l2 8H4z"/></svg>
        (757) 555-0143
      </p>
      <p class="contact-line">
        <svg viewBox="0 0 24 24" aria-hidden="true"><path d="M8 2h8a2 2 0 0 1 2 2v16a2 2 0 0 1-2 2H8a2 2 0 0 1-2-2V4a2 2 0 0 1 2-2zm0 3v7h8V5zm1 9v2h2v-2zm4 0v2h2v-2zm-4 3v2h2v-2zm4 0v2h2v-2z"/></svg>
        (757) 555-0178
      </p>
      <p class="address">582 Wexmoor Street</p>
    </section>
  </article>
</main>
</body>
</html>
```